Business card design needed

We would like a new design for our window furnishings & home decor business. We supply & install blinds, curtains, shutters etc. We are about to incorporate home decor products like cushoins & throws...
We'd like to use moderns browns & green tones. Casual but elegant style. Maybe textured/patterned look design. Design should communicate quality and great value with latest designs.

website & FB page & email is still to be advised so pls provide space.

Industry/Entity Type

Business

Contact Information for Business Card

Marlowe Haven
Window Furnishings & Home Decor
Genevieve - Interior Stylist
Call us now for a free measure & quote - 63124089
0412 906 358
0418 273 564

```html
<!DOCTYPE html>
<html lang="en">
<head>
<meta charset="utf-8">
<title>Marlowe Haven – Business Card</title>
<link rel="stylesheet" href="https://fonts.googleapis.com/css2?family=Tinos:ital,wght@0,400;0,700;1,700&display=swap">
<style>
  :root {
    --page-bg: #eceff3;
    --card-white: #ffffff;
    --card-border: #c9ccd1;
    --brown-dark: #3f2a18;
    --brown-pattern: #4a3321;
    --brown-text: #4a3220;
    --sage: #a3ad6d;
    --olive: #6b7d2e;
    --rule: #c8cfa8;
  }
  * { box-sizing: border-box; margin: 0; padding: 0; }
  html, body {
    width: 1200px; height: 1000px; overflow: hidden;
    background: var(--page-bg);
    font-family: "Tinos", "Times New Roman", serif;
  }
  .canvas { position: relative; width: 1200px; height: 1000px; }

  .card {
    position: absolute; top: 334px;
    width: 568px; height: 332px; overflow: hidden;
  }
  .card--front { left: 31px; background: var(--card-white); border: 1px solid var(--card-border); }
  .card--back { left: 610px; background: var(--brown-dark); }

  .pattern-fill {
    position: absolute; inset: 0;
    background: linear-gradient(135deg, var(--brown-pattern), var(--brown-dark));
  }

  .front-header { position: absolute; left: 0; top: 0; width: 100%; height: 113px; }
  .front-header__rule {
    position: absolute; left: 0; top: 116px; width: 100%; height: 2px; background: var(--rule);
  }
  .brand-name {
    position: absolute; color: var(--sage); font-weight: 700; letter-spacing: 0.5px;
  }
  .front-header .brand-name { left: 46px; top: 30px; font-size: 31px; }
  .brand-tagline {
    position: absolute; color: var(--sage); font-style: italic; font-weight: 700;
  }
  .front-header .brand-tagline { left: 47px; top: 68px; font-size: 16px; }

  .person-name { position: absolute; left: 46px; top: 145px; font-size: 27px; color: var(--olive); }
  .person-role { position: absolute; left: 47px; top: 174px; font-size: 16px; color: var(--brown-text); }
  .call-to-action {
    position: absolute; left: 46px; top: 208px; font-size: 15px; font-weight: 700; color: var(--olive);
  }
  .contact-list { position: absolute; left: 44px; top: 246px; list-style: none; }
  .contact-list li {
    display: flex; align-items: center; gap: 5px; height: 18px;
    font-size: 13px; color: var(--brown-text);
  }
  .contact-list svg { width: 16px; height: 16px; }

  .front-mark {
    position: absolute; left: 388px; top: 200px; width: 140px; text-align: center;
    font-size: 17px; font-weight: 700; color: var(--olive);
  }

  .back-content { position: absolute; inset: 0; text-align: center; }
  .card--back .brand-name { left: 0; width: 100%; top: 180px; font-size: 42px; }
  .card--back .brand-tagline { left: 0; width: 100%; top: 230px; font-size: 20px; }
</style>
</head>
<body>
<main class="canvas">

  <section class="card card--front" aria-label="Business card front">
    <div class="front-header">
      <div class="pattern-fill" role="img" aria-label="Subtle dark brown damask pattern"></div>
      <h1 class="brand-name">MARLOWE HAVEN</h1>
      <p class="brand-tagline">Window Furnishings &amp; Home Decor</p>
    </div>
    <div class="front-header__rule"></div>

    <h2 class="person-name">Genevieve</h2>
    <p class="person-role">Interior Stylist</p>
    <p class="call-to-action">Call us now for a free measure &amp; quote</p>

    <ul class="contact-list">
      <li>
        <svg viewBox="0 0 16 16" aria-hidden="true"><path d="M2 14 C2 6 6 2 14 2 C14 10 10 14 2 14 Z" fill="#6b7d2e"/></svg>
        phone: 63124089
      </li>
      <li>
        <svg viewBox="0 0 16 16" aria-hidden="true"><path d="M2 14 C2 6 6 2 14 2 C14 10 10 14 2 14 Z" fill="#5a3a1c"/></svg>
        mobile: 0412906358, 0418273564
      </li>
    </ul>

    <p class="front-mark">Marlowe Haven</p>
  </section>

  <section class="card card--back" aria-label="Business card back">
    <div class="pattern-fill" role="img" aria-label="Dark brown damask pattern covering the card"></div>
    <div class="back-content">
      <h2 class="brand-name">MARLOWE HAVEN</h2>
      <p class="brand-tagline">Window Furnishings &amp; Home Decor</p>
    </div>
  </section>

</main>
</body>
</html>
```